Looking for a PowerPoint design for a Pharmaceutical Company

We need a PowerPoint template design to be used company-wide. We are a pharmaceutical company with 63 years of history and want to use a new template design to work more efficiently and effectively. Below are some of the things we are looking for in the new template design.

- Simple, modern, and professional

- Practical for every day use (easy to read, easy to create)

- Slides will be mainly projected or viewed on screens, but should also work fine when printed. (e.g. We do not want to use up our inks / toners printing several pages..)

- It would be great if you could provide us a list of colors that can be effectively used in the slides. (e.g. for highlighting fonts / multiple graph colors / etc.)

- Just as an FYI, our current logo image is (dark) blue. I am not uploading the logo image here because we do not want you to be limited by the current logo image. Depending on the design, we may / may not put our logo image on the slides.

Please feel free to reach out to me if you have any questions. I look forward to seeing your design. Thank you!

Target Market(s)

Pharmaceutical industry. (To be used internally and externally)

Industry/Entity Type

Pharmaceutical

Font styles to use
Sans Serif

Requirements
Must have
• Title slide, Subtitle slide, graphs, charts, tables, bullet points, and any other slide style components normally included.
Nice to have
• - As we are in the pharma industry, we want the slides to give credibility. But we do not want it look "old", "boring", or "typical". Feel free to use unique / fresh colors.
Should not have
• - TOO many colors
• - Please do not use the images on our website, which contain faces. (Any image with faces in it...) They are stock images we bought for the website, and we do not want the images on our slides. (e.g. image of running woman on the main page, image of a surgeon, image of kids playing soccer, etc.)
• - We are not looking for a design that is a modified version of our website design. We are looking for something new.

```html
<!DOCTYPE html>
<html lang="en">
<head>
<meta charset="UTF-8">
<title>Executive Summary</title>
<link href="https://fonts.googleapis.com/css2?family=Roboto:wght@400;500;700&family=Playfair+Display+SC:wght@400&display=swap" rel="stylesheet">
<style>
  :root {
    --page-bg: #efefef;
    --title-blue: #1f4f9f;
    --rule-blue: #2a55a3;
    --cell-bg: #e0dfe0;
    --body-text: #333333;
    --footer-bg: #2a2a2a;
    --footer-text: #ffffff;
    --row-1: #062e62;
    --row-2: #083f84;
    --row-3: #0c4e9c;
    --row-4: #2463a9;
    --row-5: #2f78c4;
    --row-6: #4188d2;
  }
  * { box-sizing: border-box; margin: 0; padding: 0; }
  html, body { width: 1200px; height: 900px; overflow: hidden; }
  body {
    position: relative;
    background: var(--page-bg);
    font-family: "Roboto", Arial, sans-serif;
  }
  .slide-title {
    position: absolute;
    left: 22px; top: 22px;
    font-size: 36px;
    font-weight: 700;
    color: var(--title-blue);
    letter-spacing: 0.2px;
  }
  .brand {
    position: absolute;
    right: 20px; top: 16px;
    text-align: right;
  }
  .brand-name {
    font-size: 28px;
    font-weight: 500;
    color: var(--title-blue);
    line-height: 1.1;
  }
  .brand-tagline {
    margin-top: 6px;
    font-size: 15px;
    color: var(--title-blue);
  }
  .header-rule {
    position: absolute;
    left: 0; top: 86px;
    width: 1200px; height: 2px;
    background: var(--rule-blue);
  }
  .header-pointer {
    position: absolute;
    left: 33px; top: 87px;
  }
  .summary-table {
    position: absolute;
    left: 33px; top: 198px;
    width: 1146px;
    display: flex;
    flex-direction: column;
    gap: 1.5px;
  }
  .summary-row {
    display: flex;
    height: 105px;
  }
  .summary-label {
    width: 336px;
    display: flex;
    align-items: center;
    padding-left: 30px;
    color: #ffffff;
    font-size: 25.5px;
    font-weight: 500;
    white-space: pre;
  }
  .summary-text {
    flex: 1;
    background: var(--cell-bg);
    padding: 10px 13px 0 22px;
    font-size: 19.8px;
    line-height: 28.5px;
    color: var(--body-text);
  }
  .row-1 .summary-label { background: var(--row-1); }
  .row-2 .summary-label { background: var(--row-2); }
  .row-3 .summary-label { background: var(--row-3); }
  .row-4 .summary-label { background: var(--row-4); }
  .row-5 .summary-label { background: var(--row-5); }
  .row-6 .summary-label { background: var(--row-6); }
  .footer-bar {
    position: absolute;
    left: 0; top: 864px;
    width: 1200px; height: 36px;
    background: var(--footer-bg);
    display: flex;
    align-items: center;
    justify-content: flex-end;
    padding-right: 12px;
  }
  .footer-copyright {
    font-family: "Playfair Display SC", Georgia, serif;
    color: var(--footer-text);
    font-size: 19px;
  }
</style>
</head>
<body>
  <h1 class="slide-title">EXECUTIVE SUMMARY</h1>

  <div class="brand">
    <div class="brand-name">NOVELLA HEALTH</div>
    <div class="brand-tagline">Caring for every tomorrow</div>
  </div>

  <div class="header-rule"></div>
  <svg class="header-pointer" width="42" height="21" viewBox="0 0 42 21">
    <polygon points="0,0 42,0 21,21" fill="#2a55a3"/>
  </svg>

  <div class="summary-table">
    <div class="summary-row row-1">
      <div class="summary-label">SUMMARY TITLE  HERE</div>
      <p class="summary-text">Lorem ipsum dolor sit Lorem ipsum dolor sit&nbsp; Lorem ipsum dolor sit Lorem ipsum dolor sit&nbsp; Lorem ipsum dolor sit Lorem ipsum dolor sit&nbsp; Lorem ipsum dolor sit Lorem ipsum dolor sit</p>
    </div>
    <div class="summary-row row-2">
      <div class="summary-label">SUMMARY TITLE  HERE</div>
      <p class="summary-text">Lorem ipsum dolor sit Lorem ipsum dolor sit&nbsp; Lorem ipsum dolor sit Lorem ipsum dolor sit&nbsp; Lorem ipsum dolor sit Lorem ipsum dolor sit&nbsp; Lorem ipsum dolor sit Lorem ipsum dolor sit</p>
    </div>
    <div class="summary-row row-3">
      <div class="summary-label">SUMMARY TITLE  HERE</div>
      <p class="summary-text">Lorem ipsum dolor sit Lorem ipsum dolor sit&nbsp; Lorem ipsum dolor sit Lorem ipsum dolor sit&nbsp; Lorem ipsum dolor sit Lorem ipsum dolor sit&nbsp; Lorem ipsum dolor sit Lorem ipsum dolor sit</p>
    </div>
    <div class="summary-row row-4">
      <div class="summary-label">SUMMARY TITLE  HERE</div>
      <p class="summary-text">Lorem ipsum dolor sit Lorem ipsum dolor sit&nbsp; Lorem ipsum dolor sit Lorem ipsum dolor sit&nbsp; Lorem ipsum dolor sit Lorem ipsum dolor sit&nbsp; Lorem ipsum dolor sit Lorem ipsum dolor sit</p>
    </div>
    <div class="summary-row row-5">
      <div class="summary-label">SUMMARY TITLE  HERE</div>
      <p class="summary-text">Lorem ipsum dolor sit Lorem ipsum dolor sit&nbsp; Lorem ipsum dolor sit Lorem ipsum dolor sit&nbsp; Lorem ipsum dolor sit Lorem ipsum dolor sit&nbsp; Lorem ipsum dolor sit Lorem ipsum dolor sit</p>
    </div>
    <div class="summary-row row-6">
      <div class="summary-label">SUMMARY TITLE  HERE</div>
      <p class="summary-text">Lorem ipsum dolor sit Lorem ipsum dolor sit&nbsp; Lorem ipsum dolor sit Lorem ipsum dolor sit&nbsp; Lorem ipsum dolor sit Lorem ipsum dolor sit&nbsp; Lorem ipsum dolor sit Lorem ipsum dolor sit</p>
    </div>
  </div>

  <footer class="footer-bar">
    <span class="footer-copyright">Copyright text here</span>
  </footer>
</body>
</html>
```